Skin care manufacturer looking for packaging design for new skin care brand.

We need a design and logo for a skin care brand to be sold at retail stores and online in the United States and Europe. The design will be for 1.7oz - 2oz serums that will not have a retail box. The name of the brand is Orvia Lune and should be a luxurious brand that is approachable. The brand will consist of 4 face serums - Vitamin C, Collagen, Retinol and Hyaluronic Acid that all contain Dead Sea Minerals. Images shown are for inspiration only. Color of bottles can be varied based on design and bottles can be screen printed or labeled.

```html
<!DOCTYPE html>
<html lang="en">
<head>
<meta charset="utf-8">
<title>Orvia Lune – Vitamin C Face Serums</title>
<link href="https://fonts.googleapis.com/css2?family=Josefin+Sans:wght@400;600&family=Montserrat:wght@500;600&display=swap" rel="stylesheet">
<style>
  :root {
    --teal-deep: #178a80;
    --teal-mid: #3aa79c;
    --teal-soft: #5db4aa;
    --frost: #dfe3e2;
    --gold: #cfa335;
    --white: #ffffff;
    --ink: #0f1f1e;
  }
  html, body {
    margin: 0;
    padding: 0;
    width: 1200px;
    height: 1072px;
    overflow: hidden;
  }
  .label {
    position: relative;
    width: 1200px;
    height: 1072px;
    background: linear-gradient(180deg, var(--teal-deep) 0%, var(--teal-mid) 35%, var(--teal-deep) 62%, var(--teal-soft) 80%, var(--frost) 100%);
    display: flex;
    flex-direction: column;
    align-items: center;
    color: var(--ink);
    font-family: "Montserrat", sans-serif;
  }
  .brand-mark {
    margin-top: 110px;
    width: 170px;
    height: 170px;
    border: 7px solid var(--gold);
    border-radius: 50%;
    box-sizing: border-box;
  }
  .brand-name {
    margin: 46px 0 0;
    font-family: "Josefin Sans", sans-serif;
    font-weight: 400;
    font-size: 104px;
    line-height: 1;
    letter-spacing: 2px;
    color: var(--white);
    font-variant: small-caps;
  }
  .brand-swoosh {
    display: block;
    margin-top: 6px;
  }
  .brand-tagline {
    margin: 18px 0 0;
    font-size: 26px;
    font-weight: 500;
    letter-spacing: 9px;
  }
  .product-name {
    margin: 80px 0 0;
    text-align: center;
    font-weight: 600;
    letter-spacing: 3px;
  }
  .product-name .ingredient { display: block; font-size: 40px; }
  .product-name .category { display: block; font-size: 32px; margin-top: 8px; }
  .net-content {
    margin: 74px 0 0;
    font-size: 36px;
    font-weight: 600;
    letter-spacing: 2px;
  }
</style>
</head>
<body>
  <main class="label">
    <div class="brand-mark" aria-hidden="true"></div>
    <h1 class="brand-name">Orvia Lune</h1>
    <svg class="brand-swoosh" width="620" height="40" viewBox="0 0 620 40" aria-hidden="true">
      <path d="M10 34 Q 320 20 610 6" fill="none" stroke="var(--white)" stroke-width="5" stroke-linecap="round"/>
    </svg>
    <p class="brand-tagline">DEAD SEA MINERALS</p>
    <h2 class="product-name">
      <span class="ingredient">VITAMIN C</span>
      <span class="category">FACE SERUMS</span>
    </h2>
    <p class="net-content">2oz</p>
  </main>
</body>
</html>
```